Lantern Keepers Lantern Scribes

We would like the business card to be Horizontal
Logo on the back and want it raised.

Target Market(s)

Education and Museums

Industry/Entity Type

Education

Contact Information for Business Card

Dolores Wrenfield, P.H.D.
3918 Pelham Rd
Laurel, MD 20799
612.447.3095
Dolores.Wrenfield@lanternkeeperslanternscribes.org
lanternkeeperslanternscribes.org

Font styles to use
Serif

Colors

Designer to choose colors to be used in the design.

Requirements
Must have
• letters and logo must be raised
• Must be slate blue card
• Silver is aluminum foil

```html
<!DOCTYPE html>
<html lang="en">
<head>
<meta charset="utf-8">
<title>Lantern Keepers Lantern Scribes — Business Card</title>
<link rel="stylesheet" href="https://fonts.googleapis.com/css2?family=Crimson+Pro:wght@400;700&display=swap">
<style>
  :root {
    --page-bg: #e9e8e6;
    --card-light: #e3e7ee;
    --slate-blue: #4e5d80;
    --slate-deep: #3a4766;
    --ink: #34405c;
    --silver: #dde1e7;
    --edge-line: #c9ced6;
  }
  * { margin: 0; padding: 0; box-sizing: border-box; }
  html, body {
    width: 1200px;
    height: 900px;
    overflow: hidden;
    background: var(--page-bg);
  }
  .card {
    position: absolute;
    left: 254px;
    top: 190px;
    width: 652px;
    height: 405px;
    background: var(--card-light);
    overflow: hidden;
    font-family: "Crimson Pro", Georgia, serif;
    box-shadow: 0 2px 10px rgba(0,0,0,0.12);
  }
  .card-art {
    position: absolute;
    inset: 0;
  }
  .brand {
    position: absolute;
    left: 32px;
    top: 50px;
    width: 200px;
    height: 230px;
    color: var(--ink);
  }
  .brand-ring {
    position: absolute;
    left: 20px;
    top: 34px;
    width: 160px;
    height: 160px;
    border: 3px solid var(--ink);
    border-radius: 50%;
  }
  .brand-name {
    position: absolute;
    left: 0;
    width: 200px;
    text-align: center;
    font-weight: 700;
    font-size: 19px;
    letter-spacing: 0.6px;
    line-height: 24px;
    text-transform: uppercase;
  }
  .brand-name--top { top: 4px; }
  .brand-name--bottom { top: 202px; }
  .contact {
    position: absolute;
    right: 28px;
    top: 196px;
    text-align: right;
    color: var(--silver);
  }
  .contact-name {
    font-weight: 700;
    font-size: 25px;
    letter-spacing: 0.4px;
    line-height: 28px;
    text-transform: uppercase;
  }
  .contact-role {
    font-size: 18px;
    line-height: 22px;
    margin-bottom: 12px;
  }
  .contact-line {
    display: flex;
    justify-content: flex-end;
    align-items: center;
    gap: 6px;
    font-size: 16px;
    line-height: 25px;
    white-space: nowrap;
  }
  .contact-line svg { width: 17px; height: 17px; flex: none; }
  .contact-address {
    font-size: 16px;
    line-height: 25px;
    margin-top: 7px;
    white-space: nowrap;
  }
</style>
</head>
<body>
  <div class="card">
    <svg class="card-art" viewBox="0 0 652 405" width="652" height="405">
      <polygon points="546,0 652,0 652,405 146,405" fill="var(--slate-blue)"/>
      <polygon points="540,0 550,0 150,405 140,405" fill="var(--edge-line)"/>
      <polygon role="img" aria-label="Long rifle silhouette lying along the diagonal edge"
               points="550,0 566,0 170,405 150,405" fill="var(--slate-deep)"/>
    </svg>

    <div class="brand">
      <p class="brand-name brand-name--top">Lantern Keepers</p>
      <div class="brand-ring"></div>
      <p class="brand-name brand-name--bottom">Lantern Scribes</p>
    </div>

    <div class="contact">
      <p class="contact-name">Dolores Wrenfield</p>
      <p class="contact-role">P.H.D.</p>
      <p class="contact-line">612.447.3095
        <svg viewBox="0 0 20 20"><rect x="1.5" y="1.5" width="17" height="17" rx="3" fill="none" stroke="#dde1e7" stroke-width="1.6"/><path d="M7 5l2 2.5-1.2 1.3c.8 1.6 1.8 2.6 3.4 3.4L12.5 11 15 13l-1.3 1.8c-3.8-.3-7.2-3.7-7.5-7.5z" fill="#dde1e7"/></svg>
      </p>
      <p class="contact-line">Dolores.Wrenfield@lanternkeeperslanternscribes.org
        <svg viewBox="0 0 20 20"><rect x="1" y="4" width="18" height="12" fill="#dde1e7"/><path d="M1 4l9 7 9-7" fill="none" stroke="#4e5d80" stroke-width="1.4"/></svg>
      </p>
      <p class="contact-line">lanternkeeperslanternscribes.org
        <svg viewBox="0 0 20 20" fill="none" stroke="#dde1e7" stroke-width="1.5"><circle cx="10" cy="10" r="8.5"/><ellipse cx="10" cy="10" rx="3.6" ry="8.5"/><path d="M1.5 10h17M3 5.5h14M3 14.5h14"/></svg>
      </p>
      <p class="contact-address">3918 Pelham Rd, Laurel, MD 20799</p>
    </div>
  </div>
</body>
</html>
```